BrightLane Real Estate Sign

We are in the process of rebranding our business and need a new For Sale \ Sold sign.
We're a prestige real estate agency and therefore require a really stylish sign.
I've uploaded the following files
1. The new company logo
2. "sample sign.jpg" which shows the type of sign we would like. It is a metal sign with a top panel and bottom panel.
3. Our previous sign "previous sign.jpg" if you're interested in seeing it.
The sign must be black with white text.
Our thoughts are that the top panel (refer to sample sign) would contain the text "For Sale" or "Sold". These would be two separate panels which are interchangeable and could be screwed in place.
The bottom panel would not contain any photos like the sample. However, it may contain our logo and my contact details etc.
The sign is 900mm wide x 1200mm high.
My details are:
Name: Desmond Harlow
Web: www.blrealestate.com.au
Email: sales@blrealestate.com.au
Phone: 0491 836 205

```html
<!DOCTYPE html>
<html lang="en">
<head>
<meta charset="utf-8">
<title>BrightLane Real Estate – For Sale Sign</title>
<link rel="stylesheet" href="https://fonts.googleapis.com/css2?family=Montserrat:wght@500;600;700&display=swap">
<style>
  :root {
    --backdrop: #ececec;
    --sign-white: #ffffff;
    --panel-black: #1c1c1c;
    --headline-grey: #d6d6d6;
    --skyline-grey: #e4e4e4;
    --contact-grey: #c9c9c9;
    --ink: #111111;
  }
  * { margin: 0; padding: 0; box-sizing: border-box; }
  html, body {
    width: 1019px;
    height: 1200px;
    overflow: hidden;
    background: var(--backdrop);
    font-family: "Montserrat", sans-serif;
  }
  .sign {
    position: absolute;
    left: 40px;
    top: 250px;
    width: 944px;
    height: 701px;
  }
  .sign-top {
    position: absolute;
    left: 0; top: 0;
    width: 944px; height: 212px;
    background: var(--sign-white);
  }
  .headline-panel {
    position: absolute;
    left: 36px; top: 0;
    width: 862px; height: 206px;
    background: var(--panel-black);
    display: flex;
    align-items: center;
    justify-content: center;
  }
  .headline {
    color: var(--headline-grey);
    font-weight: 600;
    font-size: 112px;
    letter-spacing: 6px;
    word-spacing: 18px;
  }
  .sign-bottom {
    position: absolute;
    left: 4px; top: 210px;
    width: 935px; height: 491px;
    background: var(--sign-white);
  }
  .skyline-area {
    position: absolute;
    left: 33px; top: 14px;
    width: 873px; height: 190px;
    background: linear-gradient(180deg, #eeeeee 0%, var(--skyline-grey) 100%);
  }
  .brand {
    position: absolute;
    left: 33px; top: 40px;
    width: 873px;
    display: flex;
    align-items: center;
    justify-content: center;
    gap: 22px;
  }
  .brand-square {
    width: 66px; height: 66px;
    background: var(--ink);
  }
  .brand-name {
    font-weight: 700;
    font-size: 46px;
    color: var(--ink);
    letter-spacing: 0.5px;
  }
  .name-band {
    position: absolute;
    left: 39px; top: 195px;
    width: 867px; height: 56px;
    background: var(--panel-black);
    display: flex;
    align-items: center;
    justify-content: center;
  }
  .agent-name {
    color: #ececec;
    font-weight: 600;
    font-size: 38px;
    letter-spacing: 1px;
  }
  .contact-block {
    position: absolute;
    left: 48px; top: 251px;
    width: 858px; height: 212px;
    background: var(--contact-grey);
    text-align: center;
    color: var(--ink);
  }
  .phone {
    margin-top: 14px;
    font-weight: 700;
    font-size: 80px;
    letter-spacing: -1px;
    line-height: 1.1;
  }
  .email {
    margin-top: 6px;
    font-weight: 500;
    font-size: 21px;
    letter-spacing: 3px;
  }
  .website {
    margin-top: 4px;
    display: flex;
    align-items: center;
    justify-content: center;
    gap: 10px;
    font-weight: 700;
    font-size: 27px;
    letter-spacing: 1px;
  }
  .website-rule {
    width: 62px; height: 2px;
    background: var(--ink);
  }
</style>
</head>
<body>
  <div class="sign">
    <div class="sign-top">
      <div class="headline-panel">
        <span class="headline">FOR SALE</span>
      </div>
    </div>
    <div class="sign-bottom">
      <div class="skyline-area" role="img" aria-label="Faint grey city skyline silhouette behind the brand"></div>
      <div class="brand">
        <span class="brand-square"></span>
        <span class="brand-name">BrightLane Real Estate</span>
      </div>
      <div class="name-band">
        <span class="agent-name">Desmond Harlow</span>
      </div>
      <div class="contact-block">
        <div class="phone">Ph:0491 836 205</div>
        <div class="email">Email: sales@blrealestate.com.au</div>
        <div class="website">
          <span class="website-rule"></span>
          <span>www.blrealestate.com.au</span>
          <span class="website-rule"></span>
        </div>
      </div>
    </div>
  </div>
</body>
</html>
```